Amber Quill Letterhead

I just need letterhead for my integrative psychiatry business. I'm going to use this to do mailings to other doctors, as well as send letters to patients. Thank you

Industry/Entity Type

Business

```html
<!DOCTYPE html>
<html lang="en">
<head>
<meta charset="utf-8">
<title>Amber Quill Letterhead</title>
<link href="https://fonts.googleapis.com/css2?family=PT+Sans:wght@400;700&display=swap" rel="stylesheet">
<style>
  :root {
    --backdrop: #c3c4c6;
    --paper: #ebecee;
    --leaf-green: #2f7a34;
    --bark-brown: #6a3716;
    --text-green: #2d7531;
    --text-brown: #7a3a1c;
  }
  * { margin: 0; padding: 0; box-sizing: border-box; }
  html, body {
    width: 1200px;
    height: 848px;
    overflow: hidden;
    background: var(--backdrop);
    font-family: "PT Sans", sans-serif;
  }
  .letterhead {
    position: absolute;
    left: 350px;
    top: 72px;
    width: 499px;
    height: 708px;
    background: var(--paper);
  }
  .brand {
    position: absolute;
    left: 28px;
    top: 56px;
    display: flex;
    align-items: center;
    gap: 6px;
    color: var(--bark-brown);
    font-size: 17px;
    font-weight: 400;
    line-height: 1;
  }
  .brand-dot {
    width: 12px;
    height: 12px;
    border-radius: 50%;
    background: var(--leaf-green);
  }
  .contact {
    position: absolute;
    right: 16px;
    top: 34px;
    text-align: right;
    color: var(--text-green);
    font-size: 8.2px;
    line-height: 8px;
    font-style: normal;
  }
  .foliage {
    position: absolute;
    left: 20px;
    top: 640px;
    width: 144px;
    height: 48px;
    border-radius: 60px 60px 0 0;
    background: linear-gradient(180deg, #4a9a48 0%, var(--leaf-green) 100%);
  }
  .credentials {
    position: absolute;
    right: 16px;
    top: 655px;
    text-align: right;
    font-size: 8.2px;
    line-height: 7.6px;
    color: var(--text-green);
  }
  .credentials .physician { color: var(--text-brown); }
  .ground-band {
    position: absolute;
    left: 0;
    bottom: 0;
    width: 100%;
    height: 21px;
    background: var(--bark-brown);
  }
</style>
</head>
<body>
  <main class="letterhead">
    <div class="brand">
      <span class="brand-dot"></span>
      <span class="brand-name">Amber Quill</span>
    </div>

    <address class="contact">
      555-014-2206<br>
      555-014-2207<br>
      2780 Birchfield Avenue<br>
      Suite 210<br>
      Maple Glen, CA 95800<br>
      www.amberquillcare.com
    </address>

    <div class="foliage" role="img" aria-label="Illustration of green leaves sprouting from the ground"></div>

    <div class="credentials">
      <p class="physician">Helena Marsh, MD</p>
      <p>Diplomat, National Board of Mind and Brain Practice</p>
      <p>Diplomat, National Board of Integrative and Whole Health Care</p>
    </div>

    <div class="ground-band"></div>
  </main>
</body>
</html>
```